Business Card for Lorena Whitfield

Name: Lorena Whitfield
Title: Realtor
Email: Lorena@LorenaWhitfieldRE.com
Phone: 480-555-0137

On the front of the business card, I would like the photo, the contact information and the Lorena Whitfield Logo. The backside is required to have the Broker logo and the required logos. Please use the colors from the logo design. Our company has a classy, professional look.

```html
<!DOCTYPE html>
<html lang="en">
<head>
<meta charset="utf-8">
<title>Lorena Whitfield Real Estate – Business Card</title>
<link rel="stylesheet" href="https://fonts.googleapis.com/css2?family=Cinzel:wght@500&family=Open+Sans:wght@400;600&display=swap">
<style>
  :root {
    --page-bg: #e4e4e6;
    --card-dark: #232427;
    --card-light: #ffffff;
    --brand-red: #c3202f;
    --ink: #3a3a3c;
    --ink-soft: #6b6b6e;
    --white: #ffffff;
    --photo-light: #d9d9d9;
    --photo-dark: #4a4a4a;
  }
  * { box-sizing: border-box; margin: 0; padding: 0; }
  html, body { width: 1200px; height: 800px; overflow: hidden; }
  body {
    background: var(--page-bg);
    display: flex; flex-direction: column; align-items: center; justify-content: center;
    gap: 36px;
    font-family: "Open Sans", Arial, sans-serif;
  }
  .card {
    position: relative; width: 620px; height: 354px; overflow: hidden;
    box-shadow: 0 10px 28px rgba(0,0,0,.22);
  }

  /* Back side */
  .card-back { background: var(--card-dark); }
  .back-brand {
    position: absolute; left: 70px; top: 120px;
    display: flex; align-items: center; gap: 18px;
  }
  .brand-mark { width: 56px; height: 56px; border: 3px solid var(--brand-red); }
  .brand-name {
    font-family: "Cinzel", Georgia, serif; font-weight: 500;
    color: var(--brand-red); font-size: 30px; letter-spacing: 1.5px; line-height: 1.05;
  }
  .brand-name small { display: block; font-size: 15px; letter-spacing: 3px; margin-top: 4px; }
  .back-footer {
    position: absolute; right: 40px; bottom: 34px;
    display: flex; align-items: center; gap: 22px;
  }
  .broker { display: flex; align-items: center; gap: 8px; }
  .broker-dot { width: 22px; height: 22px; border-radius: 50%; border: 2px solid var(--white); }
  .broker-name {
    font-family: "Cinzel", Georgia, serif; font-weight: 500;
    color: var(--white); font-size: 13px; letter-spacing: 1.5px;
  }
  .badge { border: 2px solid var(--white); }
  .badge-a { width: 30px; height: 30px; }
  .badge-b { width: 30px; height: 30px; }
  .badge-c { width: 48px; height: 26px; }

  /* Front side */
  .card-front { background: var(--card-light); }
  .front-photo {
    position: absolute; right: 0; top: 0; width: 250px; height: 354px;
    background: radial-gradient(ellipse at 55% 35%, var(--photo-light) 0%, #a8a8a8 45%, var(--photo-dark) 100%);
  }
  .front-band {
    position: absolute; left: 0; bottom: 0; width: 370px; height: 14px;
    background: var(--brand-red);
  }
  .front-brand {
    position: absolute; left: 36px; top: 40px;
    display: flex; align-items: center; gap: 14px;
  }
  .front-brand .brand-mark { width: 44px; height: 44px; }
  .front-brand .brand-name { font-size: 23px; }
  .front-brand .brand-name small { font-size: 12px; }
  .agent { position: absolute; left: 40px; top: 150px; }
  .agent-name {
    font-family: "Cinzel", Georgia, serif; font-weight: 500;
    color: var(--brand-red); font-size: 26px; letter-spacing: 1.5px;
  }
  .agent-title { color: var(--ink-soft); font-size: 17px; margin-top: 2px; }
  .contact { list-style: none; margin-top: 20px; }
  .contact li {
    display: flex; align-items: center; gap: 10px;
    color: var(--ink); font-size: 15px; margin-bottom: 8px;
  }
  .contact svg { width: 16px; height: 16px; fill: var(--brand-red); flex: none; }
</style>
</head>
<body>

  <section class="card card-back" aria-label="Card back">
    <div class="back-brand">
      <span class="brand-mark"></span>
      <div class="brand-name">Lorena Whitfield<small>Real Estate</small></div>
    </div>
    <div class="back-footer">
      <div class="broker">
        <span class="broker-dot"></span>
        <span class="broker-name">Harlow Crest Realty</span>
      </div>
      <span class="badge badge-a" aria-label="Housing badge"></span>
      <span class="badge badge-b" aria-label="Association badge"></span>
      <span class="badge badge-c" aria-label="Listing service badge"></span>
    </div>
  </section>

  <section class="card card-front" aria-label="Card front">
    <div class="front-photo" role="img" aria-label="Black and white portrait photo of the realtor"></div>
    <div class="front-band"></div>
    <div class="front-brand">
      <span class="brand-mark"></span>
      <div class="brand-name">Lorena Whitfield<small>Real Estate</small></div>
    </div>
    <div class="agent">
      <h1 class="agent-name">Lorena Whitfield</h1>
      <p class="agent-title">Realtor</p>
      <ul class="contact">
        <li>
          <svg viewBox="0 0 24 24" aria-hidden="true"><path d="M6.6 10.8a15.1 15.1 0 0 0 6.6 6.6l2.2-2.2c.3-.3.7-.4 1-.2 1.1.4 2.3.6 3.6.6.6 0 1 .4 1 1V20c0 .6-.4 1-1 1A17 17 0 0 1 3 4c0-.6.4-1 1-1h3.5c.6 0 1 .4 1 1 0 1.3.2 2.5.6 3.6.1.3 0 .7-.2 1z"/></svg>
          480-555-0137
        </li>
        <li>
          <svg viewBox="0 0 24 24" aria-hidden="true"><path d="M2 5h20v14H2zm2 2v.5l8 5 8-5V7l-8 5z"/></svg>
          Lorena@LorenaWhitfieldRE.com
        </li>
      </ul>
    </div>
  </section>

</body>
</html>
```